Statement of Qualifications Brochure for Civil/Construction Engineering Company

We need a "statement of qualification" pdf brochure with the content that is attached and in conjuncture to the new logo we are building. We also need a logo re-design (hi-rez and color) for the logo attached.

This brochure will be sent out to companies that require information of what our company does, or for requirements in services.

We would like a black and 'runway airport blue' color scheme for the brochure and the logo. It should appear professional, easy to read, and informative.
Updates

Reason: Hello, We realize our answers to some of your questions did not come to you promptly, so we have extended this deadline by 5 days. Thank you all!

Target Market(s)

Apartment Complex ownership companies. These companies typically own 10-50 mulit-unit complexes.

Industry/Entity Type

Airport

Font styles to use
Other font styles liked:
• Would like a professional, non-decorative font

Requirements
Must have
• Sharp and easy to read. Focus on information.
Nice to have
• Nice photos, we have other photos we can send to insert if necessary

```html
<!DOCTYPE html>
<html lang="en">
<head>
<meta charset="utf-8">
<title>RK Meridian, PLLC · Statement of Qualifications · Contents</title>
<link rel="stylesheet" href="https://fonts.googleapis.com/css2?family=Barlow:wght@400;600;700&family=Jost:wght@200;300&display=swap">
<style>
  :root {
    --runway-blue: #0b8fc6;
    --line-blue: #12a9e6;
    --ink: #000000;
    --paper: #ffffff;
    --grey: #8a8a8a;
    --rule-white: #e6e6e6;
  }
  * { margin: 0; padding: 0; box-sizing: border-box; }
  html, body { width: 848px; height: 1200px; overflow: hidden; background: var(--paper); }
  .page {
    position: relative;
    width: 848px;
    height: 1200px;
    overflow: hidden;
    background: var(--paper);
    font-family: "Barlow", "Helvetica Neue", Arial, sans-serif;
  }
  .dark-field {
    position: absolute;
    left: 0; top: 197px;
    width: 848px; height: 1003px;
    background: var(--ink);
  }
  .line-art {
    position: absolute;
    inset: 0;
  }
  .running-head {
    position: absolute;
    top: 24px;
    right: 51px;
    font-size: 13.5px;
    letter-spacing: 0.01em;
    color: var(--grey);
    white-space: nowrap;
  }
  .running-head .firm { color: var(--line-blue); }
  .running-head .bold { font-weight: 700; }
  .running-head .dot,
  .page-foot .dot { font-size: 10px; vertical-align: 1px; margin: 0 3px; }
  .section-title {
    font-family: "Jost", "Helvetica Neue", Arial, sans-serif;
    font-weight: 300;
    font-size: 182px;
    fill: var(--runway-blue);
  }
  .page-foot {
    position: absolute;
    top: 1157px;
    left: 51px;
    right: 51px;
    display: flex;
    justify-content: space-between;
    font-size: 13px;
    color: var(--grey);
  }
  .page-foot .city { color: var(--line-blue); }
  .page-foot .phone { color: var(--line-blue); font-weight: 700; }
</style>
</head>
<body>
<div class="page">
  <div class="dark-field"></div>

  <svg class="line-art" width="848" height="1200" viewBox="0 0 848 1200">
    <g stroke-width="1.4" fill="none">
      <line x1="400" y1="0" x2="848" y2="446" stroke="var(--line-blue)"/>
      <line x1="53" y1="181" x2="606" y2="733" stroke="var(--line-blue)"/>
      <line x1="415" y1="723" x2="848" y2="290" stroke="var(--line-blue)"/>
      <line x1="151" y1="197" x2="482" y2="529" stroke="var(--rule-white)"/>
      <line x1="242" y1="779" x2="663" y2="1200" stroke="var(--rule-white)"/>
    </g>
    <text class="section-title" transform="translate(188,1140) rotate(-90)" textLength="643" lengthAdjust="spacingAndGlyphs">Contents</text>
  </svg>

  <header class="running-head">
    <span class="firm">RK MERIDIAN, PLLC</span><span class="dot">●</span>Statement of <span class="bold">QUALIFICATIONS</span>
  </header>

  <footer class="page-foot">
    <span class="page-number">2</span>
    <span><span class="city">Corvale, TX</span><span class="dot city">●</span><span class="phone">214.555.0147</span></span>
  </footer>
</div>
</body>
</html>
```